K&R Security Services PTY. LTD.

Ive just had my logo made and I'm looking for some simple but strong designs for my business cards the company is a security company.

Please use dark colors.

Regards,

Owen Deloit

Reason: Need more time for discussion with other directors

Industry/Entity Type

Security

Font styles to use
Sans Serif
Decorative

```html
<!DOCTYPE html>
<html lang="en">
<head>
<meta charset="utf-8">
<title>K&amp;R Security Services – Business Card</title>
<link href="https://fonts.googleapis.com/css2?family=Lato:wght@400;700&display=swap" rel="stylesheet">
<style>
  :root {
    --backdrop: #e4e4e4;
    --card: #232323;
    --card-edge: #2c2c2c;
    --pattern-a: #2a2a2a;
    --pattern-b: #1b1b1b;
    --ink: #e8e8e8;
    --ink-soft: #c9c9c9;
    --icon: #5a5a5a;
  }
  * { box-sizing: border-box; margin: 0; padding: 0; }
  html, body {
    width: 1200px; height: 1000px; overflow: hidden;
    background: var(--backdrop);
    font-family: "Lato", sans-serif;
  }
  .stage {
    position: relative; width: 1200px; height: 1000px;
  }
  .card {
    position: absolute; top: 345px;
    width: 500px; height: 310px;
    background: var(--card);
    border: 1px solid var(--card-edge);
    overflow: hidden;
    color: var(--ink);
  }
  .card--front { left: 70px; }
  .card--back { left: 630px; }

  .front-pattern {
    position: absolute; inset: 0;
    background: repeating-linear-gradient(90deg, var(--pattern-a) 0 14px, var(--pattern-b) 14px 28px);
    opacity: .8;
  }
  .brand {
    position: absolute; display: flex; align-items: center; gap: 12px;
    color: var(--ink);
  }
  .brand__dot {
    border-radius: 50%; border: 2px solid var(--ink);
  }
  .card--front .brand {
    left: 50%; top: 50%; transform: translate(-50%, -50%);
    font-size: 64px; font-weight: 400;
  }
  .card--front .brand__dot { width: 22px; height: 22px; }

  .back-decoration {
    position: absolute; right: -20px; top: -10px;
    width: 330px; height: 250px;
    background: radial-gradient(ellipse at 60% 40%, #343434 0%, var(--card) 70%);
  }
  .card--back .brand {
    left: 36px; top: 100px;
    font-size: 30px;
  }
  .card--back .brand__dot { width: 12px; height: 12px; border-width: 1.5px; }

  .contact {
    position: absolute; left: 185px; top: 88px;
  }
  .contact__name {
    font-size: 19px; letter-spacing: .5px; font-weight: 400;
    margin-bottom: 10px; margin-left: 0;
  }
  .contact__list { list-style: none; }
  .contact__item {
    display: flex; align-items: center; gap: 8px;
    font-size: 13px; color: var(--ink-soft); line-height: 23px;
  }
  .contact__item strong { font-weight: 700; color: var(--ink); }
  .icon { width: 12px; height: 12px; flex: none; }
  .address {
    position: absolute; left: 22px; right: 16px; bottom: 40px;
    display: flex; align-items: center; gap: 7px;
    font-size: 12.5px; color: var(--ink-soft); white-space: nowrap;
  }
</style>
</head>
<body>
<main class="stage">

  <section class="card card--front" aria-label="Business card front">
    <div class="front-pattern" role="img" aria-label="Repeating dark shield-shape background pattern"></div>
    <div class="brand">
      <span class="brand__dot"></span>
      <span class="brand__name">K&amp;R</span>
    </div>
  </section>

  <section class="card card--back" aria-label="Business card back">
    <div class="back-decoration" role="img" aria-label="Large faint glossy brand decoration"></div>
    <div class="brand">
      <span class="brand__dot"></span>
      <span class="brand__name">K&amp;R</span>
    </div>

    <div class="contact">
      <h1 class="contact__name">OWEN DELOIT</h1>
      <ul class="contact__list">
        <li class="contact__item">
          <svg class="icon" viewBox="0 0 12 12"><circle cx="6" cy="6" r="6" fill="var(--icon)"/><rect x="3" y="4" width="6" height="4" fill="none" stroke="#222" stroke-width="1"/><path d="M3 4l3 2.2L9 4" fill="none" stroke="#222" stroke-width="1"/></svg>
          o.deloit@krsecurity.com.au
        </li>
        <li class="contact__item">
          <svg class="icon" viewBox="0 0 12 12"><circle cx="6" cy="6" r="6" fill="var(--icon)"/><path d="M4 3.2c.6 0 1 1.3.7 1.8-.2.3.9 1.9 1.5 2.1.4-.3 1.6.2 1.6.8-.4.9-1.6 1-2.8.1C3.800 7 3 5.200 4 3.2z" fill="#222"/></svg>
          (02) 5550 1234
        </li>
        <li class="contact__item">
          <svg class="icon" viewBox="0 0 12 12"><circle cx="6" cy="6" r="6" fill="var(--icon)"/><circle cx="6" cy="6" r="3" fill="none" stroke="#222"/><path d="M3 6h6M6 3v6" stroke="#222" stroke-width=".8"/></svg>
          <span>www.<strong>krsecurity</strong>.com.au</span>
        </li>
      </ul>
    </div>

    <p class="address">
      K&amp;R Security Pty Ltd, 18 Harbour Rd, Kingsford NSW 2032
      <svg class="icon" viewBox="0 0 12 12"><circle cx="6" cy="6" r="6" fill="var(--icon)"/><path d="M4 3.2c.6 0 1 1.3.7 1.8-.2.3.9 1.9 1.5 2.1.4-.3 1.6.2 1.6.8-.4.9-1.6 1-2.8.1C3.8 7 3 5.2 4 3.2z" fill="#222"/></svg>
      (02) 5550 6789
    </p>
  </section>

</main>
</body>
</html>
```